Asset tracing and investigation firm requires marketing brochure for services

We need a professional looking brochure with layout that supports the text that we have already drafted, is easy on the eye and can easily be navigated by clients either electronic/screen format or printed format. The wording is not finalised and all aspects need to be remain editable (including the logo and picture(s)) - preferably in Word or similarly accessible format.

```html
<!DOCTYPE html>
<html lang="en">
<head>
<meta charset="utf-8">
<title>Veritrace – Asset Tracing Services Brochure</title>
<link href="https://fonts.googleapis.com/css2?family=Cinzel:wght@500;600&family=Montserrat:wght@300;400;500;600;700&display=swap" rel="stylesheet">
<style>
:root{
  --navy:#1d3f73;
  --navy-deep:#142d55;
  --blue:#2f6aa8;
  --gold:#c9a227;
  --paper:#f7f7f5;
  --ink:#2a2f38;
  --muted:#6b717b;
  --stage:#a8aaab;
}
*{box-sizing:border-box;margin:0;padding:0}
html,body{width:1200px;height:3421px;overflow:hidden}
body{background:var(--stage);font-family:"Montserrat",sans-serif;color:var(--ink)}
.section{height:684px;display:flex;align-items:center;justify-content:center}
.section + .section{border-top:1px solid #b6b8b9}
.page{position:relative;width:540px;height:382px;background:var(--paper);overflow:hidden}
.page.left{box-shadow:-4px 6px 18px rgba(0,0,0,.22);background:linear-gradient(270deg,#e6e6e3 0,var(--paper) 18px)}
.page.right{box-shadow:4px 6px 18px rgba(0,0,0,.22);background:linear-gradient(90deg,#e6e6e3 0,var(--paper) 18px)}

.brand{display:flex;align-items:center;gap:6px;font-weight:600;color:var(--navy);letter-spacing:.04em;white-space:nowrap}
.brand .mark{width:10px;height:10px;background:var(--gold)}

.cover{position:relative;width:760px;height:538px;background:var(--paper);overflow:hidden;box-shadow:0 8px 22px rgba(0,0,0,.25)}
.cover .photo{position:absolute;left:0;top:0;width:100%;height:78%;background:linear-gradient(160deg,#6fa0d6 0%,#2c5d9a 38%,#8a9aa8 62%,#c9c3b6 100%)}
.cover .band{position:absolute;right:0;bottom:0;width:60%;height:22%;background:var(--navy);display:flex;align-items:center;justify-content:space-between;padding:0 22px 0 26px}
.cover .band h1{font-family:"Cinzel",serif;font-weight:500;color:var(--gold);font-size:21px;letter-spacing:.03em;white-space:nowrap}
.cover .band .url{color:#fff;font-size:10px;letter-spacing:.05em;white-space:nowrap}
.cover .logo-box{position:absolute;left:0;bottom:0;width:40%;height:22%;display:flex;align-items:center;padding-left:40px}
.cover .logo-box .brand{font-size:30px}
.cover .logo-box .brand .mark{width:20px;height:20px}
.cover .accent{position:absolute;background:var(--navy);opacity:.85}
.cover .accent.gold{background:var(--gold);opacity:.8}
.cover.small{width:540px;height:382px}
.cover.small .band h1{font-size:14px}
.cover.small .band .url{font-size:7px}
.cover.small .band{padding:0 14px 0 16px}
.cover.small .logo-box{padding-left:26px}
.cover.small .logo-box .brand{font-size:20px}
.cover.small .logo-box .brand .mark{width:13px;height:13px}

.back .contact{position:absolute;left:36px;bottom:44px}
.back .contact .brand{font-size:24px;margin-bottom:10px}
.back .contact .brand .mark{width:15px;height:15px}
.back .contact h3{font-size:13px;font-weight:500;color:var(--navy);margin-bottom:6px}
.back .row{display:flex;gap:12px;font-size:8.5px;margin-bottom:4px;color:var(--ink);white-space:nowrap}
.back .row b{font-weight:600;width:190px;color:var(--navy)}
.back .row span{display:flex;align-items:center;gap:4px}
.back .web{font-size:10px;color:var(--navy);margin-top:6px;letter-spacing:.04em}

.footer{position:absolute;left:22px;right:22px;bottom:14px;display:flex;align-items:center;justify-content:space-between}
.footer .brand{font-size:12px}
.footer .brand .mark{width:8px;height:8px}
.footer .url{display:flex;align-items:center;gap:5px;font-size:7.5px;font-weight:600;color:var(--navy);border-bottom:1.5px solid var(--navy);padding:0 0 2px 80px;white-space:nowrap}
.footer .url i{width:9px;height:9px;border-radius:50%;background:var(--gold);display:block}
h2{font-size:13px;font-weight:500;color:var(--navy);letter-spacing:.02em;text-transform:uppercase}
h2 b{font-weight:700}
.body{font-size:5.6px;line-height:1.5;color:var(--muted)}
.body strong{color:var(--ink);font-weight:600}

.strip{position:absolute;left:0;top:0;bottom:0;width:58px;background:linear-gradient(180deg,var(--navy) 0,var(--navy-deep) 100%)}
.who .item{position:absolute;left:44px;right:28px;display:flex;gap:10px}
.icon{flex:0 0 28px;height:28px;border-radius:50%;background:var(--gold);border:2px solid #fff;display:flex;align-items:center;justify-content:center}
.who .item h2{margin-bottom:3px}

.reports{padding:26px 28px 0 26px}
.reports .text{width:250px}
.reports h2{margin-bottom:8px}
.map{position:absolute;right:0;top:0;width:180px;height:322px;background:linear-gradient(170deg,#dfe4e6 0%,#c6b89a 45%,#a9b7c0 100%)}
.bullet{display:flex;gap:6px;margin:5px 0}
.bullet .dot{flex:0 0 9px;height:9px;border-radius:2px;background:var(--navy);margin-top:1px}
.bullet p{font-size:5.4px;line-height:1.45;font-weight:600;color:var(--ink)}

.price{padding:26px 20px 0 24px}
.price h2{margin-bottom:10px}
.table{display:grid;grid-template-columns:repeat(5,1fr);height:270px;font-size:4.6px;line-height:1.5}
.col{display:flex;flex-direction:column}
.col .head{height:22px;padding:5px 4px;font-weight:700;color:#fff;text-transform:uppercase;font-size:4.4px}
.col .cell{flex:1;padding:6px 5px;color:#2c3d52}
.col .cell p{margin-bottom:5px}
.col .fee{height:16px;padding:4px 5px;font-weight:700;color:#fff;font-size:5px}
.c1 .head,.c1 .fee{background:#2b4c73}.c1 .cell{background:#dfe7ef}
.c2 .head,.c2 .fee{background:#35608a}.c2 .cell{background:#e6edf3}
.c3 .head,.c3 .fee{background:#3e7499}.c3 .cell{background:#d8e5ee}
.c4 .head,.c4 .fee{background:#4a88ab}.c4 .cell{background:#c8dde9}
.c5 .head,.c5 .fee{background:#3f8fb0}.c5 .cell{background:#5ea5c4;color:#fff}

.osint{padding:26px 0 0 26px;width:300px}
.osint h2{font-size:12px;margin-bottom:10px}
.osint .tier{margin-bottom:10px}
.osint .tier em{font-family:"Cinzel",serif;font-style:normal;font-weight:600;color:var(--navy);font-size:8px;margin-right:3px}
.director{position:absolute;right:0;top:0;bottom:0;width:210px;background:var(--navy);padding:24px 16px 0 18px;color:#fff}
.director h2{color:#fff;font-size:12px;line-height:1.2;margin-bottom:12px}
.director .who{display:flex;gap:10px;margin-bottom:12px}
.portrait{flex:0 0 52px;height:64px;background:linear-gradient(180deg,#c8cdd3,#7c8694)}
.director .name{font-size:8px;font-weight:700;color:var(--gold)}
.director .role{font-size:5px;line-height:1.5;color:#d6deea}
.director .body{color:#d6deea}
.director .footer .url{color:#fff;border-color:#fff}

.cases{padding:26px 26px 0 28px}
.cases h2{margin-bottom:6px}
.cases h4{font-size:6px;font-weight:700;color:var(--navy);text-transform:uppercase;margin:7px 0 3px}
.cases .body{font-size:4.8px}
.cases .body p{margin-bottom:2px}
</style>
</head>
<body>

<section class="section">
  <div class="cover">
    <div class="photo" role="img" aria-label="Upward view of a stone office building beside a curved glass tower against a blue sky"></div>
    <div class="accent" style="right:120px;top:40px;width:90px;height:90px"></div>
    <div class="accent" style="right:40px;top:150px;width:70px;height:70px"></div>
    <div class="accent gold" style="right:150px;top:230px;width:60px;height:60px"></div>
    <div class="accent gold" style="right:70px;top:250px;width:40px;height:40px"></div>
    <div class="logo-box"><div class="brand"><span class="mark"></span>VERITRACE</div></div>
    <div class="band"><h1>ASSET TRACING SERVICES</h1><span class="url">www.veritrace.co.uk</span></div>
  </div>
</section>

<section class="section">
  <div class="page left back">
    <div class="contact">
      <div class="brand"><span class="mark"></span>VERITRACE</div>
      <h3>After General Enquiries</h3>
      <div class="row"><b>Asset Tracing Enquiries: James Marsh</b>
        <span><svg width="8" height="8" viewBox="0 0 24 24"><path fill="#1d3f73" d="M6.6 10.8a15 15 0 006.6 6.6l2.2-2.2a1 1 0 011-.25 11.4 11.4 0 003.6.6 1 1 0 011 1V20a1 1 0 01-1 1A17 17 0 013 4a1 1 0 011-1h3.5a1 1 0 011 1c0 1.25.2 2.45.6 3.6a1 1 0 01-.25 1z"/></svg>07700 900 412</span>
        <span>j.marsh@veritrace.co.uk</span></div>
      <div class="row"><b>General Enquiries: Switchboard</b>
        <span><svg width="8" height="8" viewBox="0 0 24 24"><path fill="#1d3f73" d="M6.6 10.8a15 15 0 006.6 6.6l2.2-2.2a1 1 0 011-.25 11.4 11.4 0 003.6.6 1 1 0 011 1V20a1 1 0 01-1 1A17 17 0 013 4a1 1 0 011-1h3.5a1 1 0 011 1c0 1.25.2 2.45.6 3.6a1 1 0 01-.25 1z"/></svg>020 7946 0321</span>
        <span>hello@veritrace.co.uk</span></div>
      <div class="web">www.veritrace.co.uk</div>
    </div>
  </div>
  <div class="cover small">
    <div class="photo" role="img" aria-label="Upward view of a stone office building beside a curved glass tower against a blue sky"></div>
    <div class="accent" style="right:85px;top:28px;width:64px;height:64px"></div>
    <div class="accent" style="right:28px;top:106px;width:50px;height:50px"></div>
    <div class="accent gold" style="right:106px;top:164px;width:42px;height:42px"></div>
    <div class="logo-box"><div class="brand"><span class="mark"></span>VERITRACE</div></div>
    <div class="band"><h1>ASSET TRACING SERVICES</h1><span class="url">www.veritrace.co.uk</span></div>
  </div>
</section>

<section class="section">
  <div class="page left who">
    <div class="strip" role="img" aria-label="Dark blue tinted view of a glass tower facade"></div>
    <div class="item" style="top:22px">
      <div class="icon"><svg width="12" height="12" viewBox="0 0 24 24"><circle cx="12" cy="8" r="4" fill="#fff"/><path d="M4 21a8 8 0 0116 0z" fill="#fff"/></svg></div>
      <div><h2>Who <b>we are:</b></h2><p class="body">Veritrace are the asset tracing and investigation specialists whose intelligence and report solutions have been specifically developed for legal and corporate clients seeking professional fixed fee investigations with fast turnarounds.</p></div>
    </div>
    <div class="item" style="top:88px">
      <div class="icon"><svg width="12" height="12" viewBox="0 0 24 24"><path d="M4 12l5 5L20 6" stroke="#fff" stroke-width="3" fill="none"/></svg></div>
      <div><h2>What <b>we do:</b></h2><p class="body">In addition to tracing assets, we gather intelligence to inform your litigation strategy, bridge knowledge gaps and answer crucial questions, reducing risk and maximising recoveries. This is achieved by combining open source research, human intelligence and careful financial analysis. Our holistic approach provides maximum insight while keeping scope and fees proportionate to the matter in hand.</p></div>
    </div>
    <div class="item" style="top:170px">
      <div class="icon"><svg width="12" height="12" viewBox="0 0 24 24"><rect x="4" y="7" width="16" height="12" fill="#fff"/><rect x="9" y="4" width="6" height="4" fill="none" stroke="#fff" stroke-width="2"/></svg></div>
      <div><h2>Cases:</h2><p class="body">Clients rely on our investigation solutions on matters spanning commercial claims and disputes, civil litigation, financial fraud, enforcement of orders, claims against directors, personal injury, employee fraud, unpaid debts and loans and enforcement of personal guarantees. A handful of case studies are provided on pages 5 and 6 of this brochure.</p></div>
    </div>
    <div class="item" style="top:244px">
      <div class="icon"><svg width="12" height="12" viewBox="0 0 24 24"><rect x="5" y="3" width="14" height="18" fill="#fff"/></svg></div>
      <div><h2>Fees:</h2><p class="body">We urge all legal and corporate clients, where appropriate, to discuss cases with us from the enquiry stage so that we can scope out research possibilities, advise where we can add most value and provide a fee estimate that is proportionate to your case. Having worked on hundreds of cases, we have developed fixed price report categories. <strong>For more information please see our corresponding price &amp; service guide on page 3 of this brochure.</strong></p></div>
    </div>
    <div class="footer" style="left:70px"><div class="brand"><span class="mark"></span>VERITRACE</div><div class="url">www.veritrace.co.uk<i></i></div></div>
  </div>
  <div class="page right reports">
    <div class="text">
      <h2>‘Lattice’ <b>Asset Trace Reports:</b></h2>
      <p class="body">Our experts have developed a suite of asset tracing products to suit various budgets and scenarios, each aiming to locate specific assets, trace individuals and support enforcement.</p>
      <p class="body" style="margin-top:4px">These ‘Lattice’ reports methodically piece together findings from a range of sources to provide an overall picture of the subject, their circumstances and their assets.</p>
      <div class="bullet"><span class="dot"></span><p>Trace physical assets such as residential, investment or commercial property, holiday homes, cars and vehicles, inheritance and private company interests</p></div>
      <div class="bullet"><span class="dot"></span><p>Conduct wealth profiling analysis on their lifestyle, background, family, trading history, employment and social media analysis</p></div>
      <div class="bullet"><span class="dot"></span><p>Perform solvency due diligence through judgment, bankruptcy, credit, charges registers, court record and other database searches</p></div>
      <p class="body" style="margin-top:6px">Beyond these basic investigations, and moving through the Lattice levels, we assist on more complex cases and individuals, trace additional assets and extend the depth of intelligence gathered. Every case is unique and clients should not assume that we tailor each asset trace identically.</p>
    </div>
    <div class="map" role="img" aria-label="Map of Europe and Africa with a hand pointing and a small paper boat"></div>
    <div class="footer"><div class="brand"><span class="mark"></span>VERITRACE</div><div class="url">www.veritrace.co.uk<i></i></div></div>
  </div>
</section>

<section class="section">
  <div class="page left price">
    <h2>‘Lattice’ Price <b>&amp; Service Guide:</b></h2>
    <div class="table">
      <div class="col c1"><div class="head">Pinpoint Lattice</div><div class="cell"><p>Generally recommended where the primary focus is to trace the whereabouts of the subject.</p><p>Current address and property database enquiries.</p><p>Local enquiries.</p><p>Email report with supporting documents.</p></div><div class="fee">£450 + VAT</div></div>
      <div class="col c2"><div class="head">Snapshot Lattice</div><div class="cell"><p>Generally recommended for claims of up to £80,000.</p><p>Shorter open source enquiries.</p><p>Asset trace working on the case.</p><p>Financial analysis of most significant holdings.</p><p>Email updates on progress.</p></div><div class="fee">£800 + VAT</div></div>
      <div class="col c3"><div class="head">Focused Lattice</div><div class="cell"><p>Generally recommended for claims of up to £250,000.</p><p>Directed tier one and tier two enquiries.</p><p>Asset trace working on the case.</p><p>Site attendance and photographs.</p><p>Written report with supporting documents.</p></div><div class="fee">£1,200 + VAT</div></div>
      <div class="col c4"><div class="head">Enhanced Lattice</div><div class="cell"><p>Generally recommended for higher value cases.</p><p>Directed tier one, two and three enquiries.</p><p>International database enquiries.</p><p>Human intelligence enquiries.</p><p>Report calls to update on progress.</p></div><div class="fee">£2,000 + VAT</div></div>
      <div class="col c5"><div class="head">Investigation / International Lattice</div><div class="cell"><p>Generally recommended in complex projects across many jurisdictions.</p><p>To be discussed as per the specific needs of the investigation.</p></div><div class="fee">POA</div></div>
    </div>
    <div class="footer"><div class="brand"><span class="mark"></span>VERITRACE</div><div class="url">www.veritrace.co.uk<i></i></div></div>
  </div>
  <div class="page right">
    <div class="osint">
      <h2>Open Source Intelligence<br><b>(OSINT) Tiers:</b></h2>
      <div class="tier"><p class="body"><em>Tier One</em> OSINT sources are essential public and proprietary datasets and may include voters roll records, consumer credit files, land registry, company records, county court judgments, insolvency registers, social media footprints, telephone records and online news archives.</p></div>
      <div class="tier"><p class="body"><em>Tier Two</em> sources may be tasked discreetly and require more advanced data analysis, including human intelligence, vehicle enquiries, overseas property searches, domain and website registration, archived media and specialist employment checks.</p></div>
      <div class="tier"><p class="body"><em>Tier Three</em> sources, enacted by specialists in their respective fields, require individual asset investigation, advanced human intelligence and the use of technology and surveillance, including bank account searches and international database enquiries.</p></div>
    </div>
    <div class="director">
      <h2>Director of<br><b>Asset Tracing:</b></h2>
      <div class="who">
        <div class="portrait" role="img" aria-label="Portrait photograph of the director"></div>
        <div><div class="name">JAMES MARSH –</div><div class="role">Open Source Investigator &amp; Intelligence Specialist<br><br>Since beginning his career with an investigation firm some years ago, James has honed his skills in the manipulation of open source intelligence.</div></div>
      </div>
      <p class="body">He specialises in intelligence-led desktop and local source forensic investigation in the context of both discrete stand-alone instructions and larger projects. As a result, our range of Lattice reports benefits from his unique skill set and experience across hundreds of UK and international asset tracing cases.</p>
      <p class="body" style="margin-top:5px">As well as contentious civil litigation, James's experience spans business intelligence, compliance and due diligence projects.</p>
      <div class="footer" style="left:18px;right:16px;justify-content:flex-end"><div class="url" style="padding-left:60px">www.veritrace.co.uk<i></i></div></div>
    </div>
    <div class="footer" style="right:230px"><div class="brand"><span class="mark"></span>VERITRACE</div></div>
  </div>
</section>

<section class="section">
  <div class="page left cases">
    <h2>‘Lattice’ <b>Asset Trace Reports:</b></h2>
    <h4>UK location trace and asset search investigation</h4>
    <div class="body"><p><strong>Client:</strong> Law Firm</p><p><strong>Scenario:</strong> The client had obtained judgment in a UK court following the collapse of a business venture. Significant assets had been moved and the debtor was believed to be abroad.</p><p><strong>Result:</strong> The subject was traced to a property owned through a family company and several undisclosed holdings were identified, allowing enforcement to proceed.</p></div>
    <h4>Overseas location trace and asset search investigation</h4>
    <div class="body"><p><strong>Client:</strong> Law Firm</p><p><strong>Scenario:</strong> The client had advanced funds to an associate who relocated overseas after a specified period without repaying the loan.</p><p><strong>Result:</strong> We traced the subject's new residence and identified business interests abroad, enabling the client to pursue a suitable recovery strategy.</p></div>
    <h4>Personal injury pre-sue report</h4>
    <div class="body"><p><strong>Client:</strong> Law Firm</p><p><strong>Scenario:</strong> The claimant had been injured in an incident and the client needed to know whether the defendant could satisfy a judgment before issuing proceedings.</p><p><strong>Result:</strong> Our enquiries established that the defendant held sufficient property equity and an active trading business, so the client proceeded with confidence.</p></div>
    <div class="footer"><div class="brand"><span class="mark"></span>VERITRACE</div><div class="url">www.veritrace.co.uk<i></i></div></div>
  </div>
  <div class="page right cases">
    <h4 style="margin-top:0">Lender calling on personal guarantees</h4>
    <div class="body"><p><strong>Client:</strong> Law Firm</p><p><strong>Scenario:</strong> The client had lent money to a development company secured by personal guarantees from its directors, and the company later failed.</p><p><strong>Result:</strong> We identified properties held by each guarantor and reported on equity available to meet the guarantees.</p></div>
    <h4>Lender calling on personal guarantees</h4>
    <div class="body"><p><strong>Client:</strong> Specialist Lender</p><p><strong>Scenario:</strong> A borrower defaulted and the guarantors claimed they held no assets of any value in the United Kingdom.</p><p><strong>Result:</strong> Our report revealed investment property and company shareholdings, and the guarantors agreed a settlement shortly afterwards.</p></div>
    <h4>Investigations in defence of a claim</h4>
    <div class="body"><p><strong>Client:</strong> Insurer</p><p><strong>Scenario:</strong> A claimant alleged significant lost earnings following an accident and the client sought independent verification of the losses.</p><p><strong>Result:</strong> We found evidence of continued trading and income, which the client used to robustly challenge the value of the claim.</p></div>
    <h4>Use of an alias – asset trace</h4>
    <div class="body"><p><strong>Client:</strong> Solicitor</p><p><strong>Scenario:</strong> The debtor had operated under a different name to avoid creditors and had moved address several times.</p><p><strong>Result:</strong> We linked both identities and located the debtor with assets sufficient to satisfy the debt.</p></div>
    <div class="footer"><div class="brand"><span class="mark"></span>VERITRACE</div><div class="url">www.veritrace.co.uk<i></i></div></div>
  </div>
</section>

</body>
</html>
```